Postcard Design

I need a post card design for my company. We are a Keystone Property Company.

We are looking for real estate agents who have a California Real Estate license but are not active with SPC ( Office of Land Permits).

When they join Brightpath Realty they do not have to join the Guild of HOMESELLERS. This will save them hundreds to thousands of dollars fees a year. They will become a referral real estate agent.

The cost to join Brightpath Realty is $20.00 per month and a one time $75.00 sign up fee.

All agents who join will get a 90% commission split on all referrals. They will get 80% to 90% split on all sales generated.

We will provide business cards and coaching for FREE.

Contact information.

MARTIN DELLAVEQ |JD
Founder & Owner
CA. Broker License #948172
800-452-3186
BrightpathRealty@mailcove.test
www.BrightpathRealty.test

Target Market(s)

Real estate agents in California

Industry/Entity Type

Real Estate

Font styles to use
Serif

Colors
0255a3
f37122

Requirements
Must have
• I need my logo and photo of me. Use the other photo in the design too.

Nice to have
• Here is something to use.
WE WANT TO BE YOUR PARTNER!

WHY SHOULD YOU HANG YOUR LICENSE WITH
BRIGHTPATH REALTY?
• NON MORE BOARD OR MLS DUES!
• BECOME A REFERRAL AGENT!
• EARN REFERRAL COMMISSIONS!
• SELL NEW HOMES & EARN FULL COMMISSIONS!
• KEEP YOUR LICENSE ACTIVE
Visit our web-site
http://www.BrightpathRealty.test
You can earn thousands of Dollars by being a referring agent for a small monthly fee of $20.00 per month.
Commission’s splits start at 90%.
Call for more information on how you can keep you license active without paying local board dues and MLS fees!
(800) 452-3186

```html
<!DOCTYPE html>
<html lang="en">
<head>
<meta charset="utf-8">
<title>Brightpath Realty Postcard</title>
<link rel="stylesheet" href="https://fonts.googleapis.com/css2?family=Marcellus&family=Tinos&family=Arimo:wght@400;700&family=Roboto+Condensed:wght@700&family=Lato:wght@700&display=swap">
<style>
  :root {
    --blue: #0a4f9e;
    --blue-deep: #0255a3;
    --orange: #f37122;
    --orange-bar: #ef7d22;
    --orange-soft: #f9a560;
    --navy: #2a2466;
    --ink: #1b1b1b;
    --white: #ffffff;
    --stage: #1c1c1c;
  }
  * { margin: 0; padding: 0; box-sizing: border-box; }
  html, body { width: 815px; height: 1200px; overflow: hidden; background: var(--stage); }
  .canvas { position: relative; width: 815px; height: 1200px; }
  .card { position: absolute; left: 65px; width: 682px; background: var(--white); overflow: hidden; }
  .card--front { top: 63px; height: 528px; }
  .card--back { top: 608px; height: 529px; }

  .edge-strip { position: absolute; left: 0; top: 0; width: 12px; height: 135px; background: var(--blue); }

  .brand { position: absolute; left: 20px; top: 142px; width: 202px; display: flex; align-items: center; gap: 7px; }
  .brand__square { width: 18px; height: 18px; flex: none; background: var(--orange); }
  .brand__name { font-family: "Marcellus", serif; font-size: 19px; color: var(--navy); white-space: nowrap; }

  .headline { position: absolute; left: 228px; top: 0; width: 454px; height: 134px; background: var(--blue); color: var(--white); text-align: center; font-family: "Marcellus", serif; }
  .headline__small { display: block; font-size: 26px; letter-spacing: 1px; padding-top: 29px; }
  .headline__large { display: block; font-size: 46px; letter-spacing: 1px; line-height: 1.1; }

  .money-photo { position: absolute; left: 228px; top: 134px; width: 454px; height: 394px;
    background: linear-gradient(160deg, #f4f5f3 0%, #e9ebe7 45%, #f6f6f4 100%); }

  .profile { position: absolute; left: 13px; top: 192px; width: 201px; height: 336px; background: var(--orange-soft); }
  .profile__photo { position: absolute; left: 46px; top: 9px; width: 104px; height: 122px; border-radius: 8px;
    background: linear-gradient(180deg, #3f7ac2 0%, #6f95c4 55%, #2b2f3a 100%); }
  .profile__bio { position: absolute; left: 8px; top: 145px; width: 185px; font-family: "Tinos", serif; font-size: 11.3px; line-height: 14.2px; text-align: justify; color: var(--ink); }
  .site-bar { position: absolute; left: 13px; top: 466px; width: 201px; height: 34px; background: var(--orange-bar); font-family: "Arimo", sans-serif; font-size: 14px; color: var(--navy); line-height: 34px; text-align: center; white-space: nowrap; }

  .pitch { position: absolute; left: 228px; top: 192px; width: 454px; color: var(--ink); }
  .pitch__question { font-family: "Marcellus", serif; font-size: 15px; }
  .pitch__list { list-style: none; margin: 13px 0 0 40px; font-family: "Marcellus", serif; font-size: 15px; line-height: 20.4px; }
  .pitch__offer { margin-top: 17px; font-family: "Lato", sans-serif; font-weight: 700; font-size: 14.5px; line-height: 19px; }
  .pitch__split { margin-top: 9px; font-family: "Lato", sans-serif; font-weight: 700; font-size: 14.5px; }
  .pitch__note { margin-top: 21px; font-family: "Arimo", sans-serif; font-size: 12px; line-height: 15.5px; }

  .call-bar { position: absolute; left: 228px; top: 466px; width: 454px; height: 34px; background: var(--orange-bar); color: var(--white); font-family: "Roboto Condensed", sans-serif; font-weight: 700; font-size: 19px; display: flex; align-items: center; justify-content: flex-end; gap: 8px; padding-right: 32px; }
  .call-bar svg { width: 18px; height: 18px; }

  .about { position: absolute; left: 229px; top: 0; width: 264px; height: 135px; background: var(--blue); color: var(--white); font-family: "Arimo", sans-serif; font-size: 10.3px; line-height: 13.5px; padding: 38px 10px 0 11px; }
  .about p + p { margin-top: 13px; }

  .biz-card { position: absolute; left: 13px; top: 192px; width: 309px; height: 233px; border-radius: 8px; overflow: hidden; background: var(--blue); color: var(--white); }
  .biz-card__title { text-align: center; font-family: "Marcellus", serif; }
  .biz-card__small { display: block; font-size: 16px; letter-spacing: 1px; padding-top: 8px; }
  .biz-card__large { display: block; font-size: 26px; letter-spacing: .5px; line-height: 1.1; }
  .biz-card__photo { position: absolute; left: 30px; top: 76px; width: 86px; height: 101px; border-radius: 7px;
    background: linear-gradient(180deg, #3f7ac2 0%, #6f95c4 55%, #2b2f3a 100%); }
  .biz-card__details { position: absolute; left: 141px; top: 78px; width: 162px; font-family: "Marcellus", serif; font-size: 12px; line-height: 15px; }
  .biz-card__contact { margin-top: 18px; display: flex; align-items: center; gap: 6px; white-space: nowrap; }
  .biz-card__contact + .biz-card__contact { margin-top: 6px; }
  .biz-card__contact svg { width: 11px; height: 11px; flex: none; }
  .biz-card__email { font-size: 9.5px; letter-spacing: -.2px; }
  .biz-card__site { position: absolute; left: 0; top: 193px; width: 100%; height: 31px; background: var(--orange-bar); color: var(--navy); font-family: "Arimo", sans-serif; font-size: 17px; text-align: center; line-height: 31px; }
</style>
</head>
<body>
<div class="canvas">

  <section class="card card--front">
    <div class="edge-strip"></div>
    <div class="brand"><span class="brand__square"></span><span class="brand__name">Brightpath Realty</span></div>

    <header class="headline">
      <span class="headline__small">WE WANT TO BE</span>
      <span class="headline__large">YOUR PARTNER !</span>
    </header>

    <div class="money-photo" role="img" aria-label="Faded stacks of dollar banknotes"></div>

    <aside class="profile">
      <div class="profile__photo" role="img" aria-label="Portrait photo of the company founder"></div>
      <p class="profile__bio">Martin Dellaveq, the Founder and Broker of Brightpath Realty Group, has been a California Real Estate Broker since 1978. Martin Dellaveq is also a licensed Real Estate Broker in Nevada since 2001. He earned his Juris Doctor Degree from Harbor Crest University College of Law in 1986.</p>
    </aside>
    <div class="site-bar">www.brightpathrealty.test</div>

    <div class="pitch">
      <p class="pitch__question">Why should you hang your license with BRIGHTPATH REALTY?</p>
      <ul class="pitch__list">
        <li>No More Board or MLS Dues !</li>
        <li>Become a Referral Agent !</li>
        <li>Earn Referral Commissions !</li>
        <li>Sell New homes &amp; Earn Full Commissions !</li>
        <li>Keep Your License Active !</li>
      </ul>
      <p class="pitch__offer">You can earn thousands of Dollars by being a referring agent for a small monthly fee of $20.00 per month.</p>
      <p class="pitch__split">Commission’s splits start at 90%.</p>
      <p class="pitch__note">Call for more information on how you can keep you license active without paying local board dues and MLS fees!</p>
    </div>

    <div class="call-bar">
      <svg viewBox="0 0 24 24" aria-hidden="true"><path fill="#1d5fb4" d="M6.6 10.8a15.1 15.1 0 0 0 6.6 6.6l2.2-2.2c.3-.3.7-.4 1-.2 1.1.4 2.3.6 3.6.6.6 0 1 .4 1 1V20c0 .6-.4 1-1 1A17 17 0 0 1 3 4c0-.6.4-1 1-1h3.5c.6 0 1 .4 1 1 0 1.3.2 2.5.6 3.6.1.3 0 .7-.2 1z"/></svg>
      <span>Call Us Now : (800) 452-3186</span>
    </div>
  </section>

  <section class="card card--back">
    <div class="edge-strip"></div>
    <div class="brand"><span class="brand__square"></span><span class="brand__name">Brightpath Realty</span></div>

    <div class="about">
      <p><strong>Brightpath Realty Group</strong> is the best alternative for you to continue to generate commissions without having to turn you real estate license into the SPC.</p>
      <p>You worked very hard to get your California Real Estate License don't waste it use it!</p>
    </div>

    <div class="biz-card">
      <div class="biz-card__title">
        <span class="biz-card__small">WE WANT TO BE</span>
        <span class="biz-card__large">YOUR PARTNER !</span>
      </div>
      <div class="biz-card__photo" role="img" aria-label="Portrait photo of the company founder"></div>
      <div class="biz-card__details">
        <p>MARTIN DELLAVEQ |JD</p>
        <p>Founder &amp; Owner</p>
        <p>CA. Broker License #948172</p>
        <p class="biz-card__contact">
          <svg viewBox="0 0 24 24" aria-hidden="true"><path fill="#fff" d="M6.6 10.8a15.1 15.1 0 0 0 6.6 6.6l2.2-2.2c.3-.3.7-.4 1-.2 1.1.4 2.3.6 3.6.6.6 0 1 .4 1 1V20c0 .6-.4 1-1 1A17 17 0 0 1 3 4c0-.6.4-1 1-1h3.5c.6 0 1 .4 1 1 0 1.3.2 2.5.6 3.6.1.3 0 .7-.2 1z"/></svg>
          <span>800-452-3186</span>
        </p>
        <p class="biz-card__contact">
          <svg viewBox="0 0 24 24" aria-hidden="true"><rect x="2" y="5" width="20" height="14" fill="none" stroke="#fff" stroke-width="2"/><path d="M2 5l10 8 10-8" fill="none" stroke="#fff" stroke-width="2"/></svg>
          <span class="biz-card__email">BrightpathRealty@mailcove.test</span>
        </p>
      </div>
      <div class="biz-card__site">www.brightpathrealty.test</div>
    </div>
  </section>

</div>
</body>
</html>
```